Asia based real estate financing firm needs and AWESOME design for a biz card -Harbor Lending Circle

Looking for a stylish, & corporate-looking business card for a real estate financing brokerage firm in Asia, offering global mortgage loans. I uploaded our current logos. We would like to add a splash of color (perhaps the house icon) or any other suggestions are open. For the winning designer, we have a lot of work! Thanks and best of luck!

Target Market(s)

Real estate investors globally. We want to look more like a BANK and NOT a real estate company. Please don't play up on a "house" design.

Industry/Entity Type

Banking

Contact Information for Business Card

Harbor Lending Circle
Peter Wilks
Co-Founder | Partner

14 Cassia Lane, Suite 310
Singapore 047219
www.hlc-example.asia
peterwilks@hlc-example.asia
+65 555-0142
WeChat: peterwilks

Colors

Designer to choose colors to be used in the design.

Requirements
Must have
• Must have the standard business requirements for a card; name, address, email, etc
• Can be horizontal or vertical.
Nice to have
• It would be great to see some sort of variation to the logo with a pop of color. Red is good as we're in Asia, however, other options work as well.
• Our tag line is - Borderless mortgages. It doesn't have to be on the card but might be nice.
• I'd like to start seeing our tagline within the cards as well. - Borderless mortgages.
• Also, please add our location. The location for this card is Singapore so perhaps it can be highlighted or emphasised in some way.
• Singapore | Hong Kong | Shanghai | Manila
• As we will soon open an office in Shanghai, having an option for both languages would be great.
Should not have
• I'm exceited and open to your creativity ... knock it out of the park!

```html
<!DOCTYPE html>
<html lang="en">
<head>
<meta charset="utf-8">
<title>Harbor Lending Circle – Business Card</title>
<link rel="stylesheet" href="https://fonts.googleapis.com/css2?family=Lato:wght@400;700&display=swap">
<style>
  :root {
    --backdrop: #d9d9d9;
    --card: #000000;
    --ink: #ffffff;
    --band: #ffffff;
    --band-ink: #111111;
  }
  * { margin: 0; padding: 0; box-sizing: border-box; }
  html, body { width: 1200px; height: 1200px; overflow: hidden; }
  body {
    background: var(--backdrop);
    font-family: "Lato", sans-serif;
    color: var(--ink);
    position: relative;
  }
  .card {
    position: absolute;
    left: 172px;
    width: 846px;
    height: 482px;
    background: var(--card);
    border-radius: 26px;
    overflow: hidden;
  }
  .card--front { top: 94px; }
  .card--back { top: 612px; }

  .brand {
    position: absolute;
    left: 0; right: 0;
    display: flex;
    flex-direction: column;
    align-items: center;
  }
  .brand__mark { background: var(--ink); }
  .brand__name { font-weight: 400; letter-spacing: 0.04em; white-space: nowrap; }

  .card--front .brand { top: 44px; gap: 26px; }
  .card--front .brand__mark { width: 22px; height: 22px; }
  .card--front .brand__name { font-size: 50px; }

  .card--back .brand { top: 46px; gap: 44px; }
  .card--back .brand__mark { width: 36px; height: 36px; }
  .card--back .brand__name { font-size: 64px; }

  .person {
    position: absolute;
    right: 456px;
    top: 266px;
    text-align: right;
    white-space: nowrap;
  }
  .person__name { font-size: 37px; line-height: 1.1; }
  .person__role { font-size: 26px; line-height: 1.4; }

  .divider {
    position: absolute;
    left: 424px;
    top: 246px;
    width: 2px;
    height: 120px;
    background: var(--ink);
  }

  .contacts {
    position: absolute;
    left: 460px;
    top: 235px;
    list-style: none;
  }
  .contacts li {
    display: flex;
    align-items: center;
    height: 34.5px;
    font-size: 19px;
    white-space: nowrap;
  }
  .contacts svg { width: 22px; height: 22px; margin-right: 12px; flex: none; }

  .address-band {
    position: absolute;
    left: 0; right: 0;
    top: 415px;
    height: 37px;
    background: var(--band);
    color: var(--band-ink);
    font-weight: 700;
    font-size: 24px;
    display: flex;
    align-items: center;
    justify-content: center;
  }

  .web-line {
    position: absolute;
    left: 0; right: 0;
    top: 410px;
    text-align: center;
    font-size: 32px;
  }
</style>
</head>
<body>
  <section class="card card--front" aria-label="Card front">
    <div class="brand">
      <span class="brand__mark"></span>
      <span class="brand__name">Harbor Lending Circle</span>
    </div>

    <div class="person">
      <p class="person__name">Peter Wilks</p>
      <p class="person__role">Co-Founder | Partner</p>
    </div>

    <div class="divider"></div>

    <ul class="contacts">
      <li>
        <svg viewBox="0 0 24 24" aria-hidden="true"><path fill="#fff" d="M6.6 3.5l3 3.2-1.8 2.1c1.2 2.6 3.2 4.6 5.8 5.8l2.1-1.8 3.2 3-1.9 3c-7.3-.6-12.8-6.1-13.4-13.4z"/></svg>
        +65 555-0142
      </li>
      <li>
        <svg viewBox="0 0 24 24" aria-hidden="true"><rect x="2" y="5" width="20" height="14" rx="1.5" fill="#fff"/><path d="M3 6.5l9 6.5 9-6.5" fill="none" stroke="#000" stroke-width="1.8"/></svg>
        peterwilks@hlc-example.asia
      </li>
      <li>
        <svg viewBox="0 0 24 24" aria-hidden="true"><circle cx="12" cy="12" r="10" fill="#fff"/><path d="M5 8c2 0 3 1 3 3s2 2 2 4-1 3-1 5M14 3c0 2 1 3 3 3s2 2 3 4M16 14c1 0 2 1 2 3" fill="none" stroke="#000" stroke-width="1.6"/></svg>
        www.hlc-example.asia
      </li>
      <li>
        <svg viewBox="0 0 24 24" aria-hidden="true"><circle cx="12" cy="12" r="9" fill="none" stroke="#fff" stroke-width="2"/></svg>
        peterwilks
      </li>
    </ul>

    <div class="address-band">14 Cassia Lane, Suite 310 Singapore 047219</div>
  </section>

  <section class="card card--back" aria-label="Card back">
    <div class="brand">
      <span class="brand__mark"></span>
      <span class="brand__name">Harbor Lending Circle</span>
    </div>
    <p class="web-line">www.hlc-example.asia</p>
  </section>
</body>
</html>
```